Plumbing Company business card design

Create a business card for our plumbing company. Following info needs to be present

Website-rivertoptapworks.net
Email- rivertoptapworks@mailnest.net
Phone-555-314-2098
Address-4876 NW Larkspur Blvd STE K
Fernvale, Lakeland 50999

```html
<!DOCTYPE html>
<html lang="en">
<head>
<meta charset="utf-8">
<title>Rivertop Tapworks – Business Card</title>
<link rel="stylesheet" href="https://fonts.googleapis.com/css2?family=Montserrat:wght@500;700&family=Roboto:wght@400;500&display=swap">
<style>
  :root {
    --red: #ee2127;
    --blue: #0b4fae;
    --deep-blue: #0a3a9a;
    --white: #ffffff;
    --ink: #222222;
    --stage: #cbc8c9;
  }
  * { margin: 0; padding: 0; box-sizing: border-box; }
  html, body { width: 1200px; height: 900px; overflow: hidden; }
  body {
    background: var(--stage);
    display: flex;
    flex-direction: column;
    align-items: center;
    justify-content: center;
    gap: 60px;
    font-family: "Roboto", Arial, sans-serif;
  }
  .card {
    position: relative;
    width: 620px;
    height: 354px;
    overflow: hidden;
    box-shadow: 0 6px 18px rgba(0,0,0,0.18);
  }
  .card-front { background: var(--white); }
  .front-shapes { position: absolute; inset: 0; }
  .brand {
    position: absolute;
    left: 70px;
    top: 44px;
    display: flex;
    align-items: center;
    gap: 12px;
  }
  .brand-dot {
    width: 40px; height: 40px;
    border-radius: 50%;
    background: var(--red);
  }
  .brand-name {
    font-family: "Montserrat", sans-serif;
    font-weight: 700;
    font-size: 22px;
    letter-spacing: 1px;
    text-transform: uppercase;
    color: var(--blue);
  }
  .holder {
    position: absolute;
    right: 34px;
    top: 118px;
    text-align: right;
  }
  .holder-name {
    font-family: "Montserrat", sans-serif;
    font-weight: 700;
    font-size: 18px;
    letter-spacing: 1px;
    color: var(--blue);
    text-transform: uppercase;
  }
  .holder-role {
    font-family: "Montserrat", sans-serif;
    font-weight: 500;
    font-size: 11px;
    letter-spacing: 2px;
    color: var(--ink);
    margin-top: 4px;
  }
  .contact-list {
    position: absolute;
    left: 26px;
    top: 174px;
    list-style: none;
    color: var(--white);
    font-size: 14px;
  }
  .contact-list li {
    display: flex;
    align-items: center;
    gap: 10px;
    margin-bottom: 10px;
  }
  .contact-list svg { width: 14px; height: 14px; flex: none; }
  .address {
    position: absolute;
    right: 34px;
    top: 248px;
    text-align: right;
    color: var(--white);
    font-size: 14px;
    line-height: 1.45;
    font-style: normal;
  }
  .card-back {
    background: linear-gradient(115deg,
      var(--deep-blue) 0%, #5a3f8f 22%, var(--red) 42%,
      var(--red) 52%, #c23a5a 66%, var(--blue) 100%);
    display: flex;
    align-items: center;
    justify-content: center;
    gap: 22px;
  }
  .back-dot {
    width: 86px; height: 86px;
    border-radius: 50%;
    background: var(--white);
  }
  .back-name {
    font-family: "Montserrat", sans-serif;
    font-weight: 700;
    font-size: 40px;
    letter-spacing: 2px;
    text-transform: uppercase;
    color: var(--white);
    line-height: 1.1;
  }
</style>
</head>
<body>

<section class="card card-front" aria-label="Business card front">
  <svg class="front-shapes" viewBox="0 0 620 354" aria-hidden="true">
    <polygon class="band-red" points="0,150 367,150 250,354 0,354" fill="var(--red)"/>
    <path class="band-blue" d="M270,354 L345,224 Q360,200 388,200 H620 V354 Z" fill="var(--blue)"/>
  </svg>

  <div class="brand">
    <span class="brand-dot"></span>
    <span class="brand-name">Rivertop Tapworks</span>
  </div>

  <div class="holder">
    <p class="holder-name">Marcus Elwood</p>
    <p class="holder-role">DIRECTOR</p>
  </div>

  <ul class="contact-list">
    <li>
      <svg viewBox="0 0 24 24" aria-hidden="true"><path fill="currentColor" d="M6.6 10.8a15.1 15.1 0 0 0 6.6 6.6l2.2-2.2a1 1 0 0 1 1-.25 11.4 11.4 0 0 0 3.6.57 1 1 0 0 1 1 1V20a1 1 0 0 1-1 1A17 17 0 0 1 3 4a1 1 0 0 1 1-1h3.5a1 1 0 0 1 1 1c0 1.25.2 2.45.57 3.57a1 1 0 0 1-.25 1z"/></svg>
      <span>555-314-2098</span>
    </li>
    <li>
      <svg viewBox="0 0 24 24" aria-hidden="true"><path fill="none" stroke="currentColor" stroke-width="2" d="M3 5h18v14H3z M3 5l9 8 9-8"/></svg>
      <span>rivertoptapworks@mailnest.net</span>
    </li>
    <li>
      <svg viewBox="0 0 24 24" aria-hidden="true"><g fill="none" stroke="currentColor" stroke-width="2"><circle cx="12" cy="12" r="9"/><path d="M3 12h18M12 3c3 3 3 15 0 18M12 3c-3 3-3 15 0 18"/></g></svg>
      <span>rivertoptapworks.net</span>
    </li>
  </ul>

  <address class="address">
    4876 NW<br>
    Larkspur Blvd STE K<br>
    Fernvale, Lakeland 50999
  </address>
</section>

<section class="card card-back" aria-label="Business card back">
  <span class="back-dot"></span>
  <span class="back-name">Rivertop<br>Tapworks</span>
</section>

</body>
</html>
```